Corvella Website Homepage

Committed to delivering quality content, quillpagewords.com is a content providing company. Equipped with resourceful writers with industry experience, we promise to empower our clients with content that is tailor-made to address specific requirements of their target Audience.

We need a website home page and one internal page designed. It is very important that the page be laid out with SEO in mind. We like the idea of using five images as navigation to our services. The five major services we offer are:
• Web Content writing (articles, features, website copy etc)
• Business Content writing (Press release, mailers & flyers, brochure/catalog)
• Personal Content writing (blog, speech writing)
• Hire a writer/editor
• Proof reading and editing services
The sample template (http://pv7.layoutdemo-hub.net/dx_48270/index.html) included has five images in the first fold. Designer can choose the right image for each service and lay over the service name on the image. Please do not use flash ( We will use javascripts). We need to have a detailed right side nav as in the template for SEO reasons. There will be some marketing ad- copy below the main images. Followed by a 200 character SEO optimized text defining our services in further detail. Apart from these a designer is free to use his creativity. The name of the site will be http://www.quillpagewords.com/. This name will need a logo too. Please include it as part of design. Corvellacorp is the owner of quillpagewords.com. We already have a logo for Corvella that is attached here as a separate file.

We have some taglines that need to be incorporated in the home page and other pages.
Please provide link button for Home, About us, Services, Samples, Pricing, Clients, Career, Contact us.

Links can be given on TOP, Sideways and Bottom and in the drop down menu of services etc.

Reason: Hi

We have made our project guaranteed and extended deadline by 5 days so you get more time to complete our project.

Thanks and Regards,

Ravindra Kulkarni
Corvellacorp

Target Market(s)

Product Marketing Companies - Mostly in US.
Media companies which publish articles on various subjects. Travel and Lifestyle related sites, Educational Websites, Government Websites, Health related websites,

Industry/Entity Type

Marketing

Requirements
Must have
• Color of Homepage should blend with sober mood of the content. Writing Services should get highlighted in such a way that any person serious about the business visiting the site get attracted to read on the details of our content services. Most space should be used for details of writing services and links for our various pages and services. Webpage should be downloaded in lowest possible time.
Nice to have
• We have some idea about the website layouts;-http://www.skinbazaarly.net/site-layouts/48270.html - layout of information http://www.skinbazaarly.net/site-layouts/47359.html - for kind of marketing http://pv7.layoutdemo-hub.net/dx_48615/index.html - for colors
we attach a word file representing our idea in some way but not limited to it.
Should not have
• Gaudy (aggressive dark) colors. It should not be cluttered. No flash.

```html
<!DOCTYPE html>
<html lang="en">
<head>
<meta charset="utf-8">
<title>Quillpage Words – Home</title>
<link href="https://fonts.googleapis.com/css2?family=Arimo:wght@400;700&family=Open+Sans:wght@400;600&display=swap" rel="stylesheet">
<style>
:root{
  --accent-green:#a8e08f;
  --header-top:#121212;
  --header-bottom:#3c3c3c;
  --nav-active:#c3303b;
  --brand-blue:#1d74a3;
  --brand-red:#c8313b;
  --text:#333;
  --green-box:#d3f9c9;
  --green-title:#1f7b14;
  --blue-box:#c9ecfb;
  --blue-title:#134c70;
  --link:#1b4f73;
  --footer:#333;
  --copyright:#b8e28b;
}
*{margin:0;padding:0;box-sizing:border-box}
html,body{width:1200px;height:1001px;overflow:hidden;background:#fff}
body{position:relative;font-family:Arimo,Arial,sans-serif;color:var(--text);font-size:12px}
.top-strip{position:absolute;left:0;top:0;width:1200px;height:9px;background:var(--accent-green)}
.masthead{position:absolute;left:0;top:9px;width:1200px;height:431px;background:linear-gradient(var(--header-top),var(--header-bottom))}
.site-logo{position:absolute;left:106px;top:18px;display:flex;align-items:center;gap:12px}
.site-logo .dot{width:54px;height:54px;border-radius:50%;background:var(--brand-blue)}
.site-logo .name{color:#fff;font-family:"Open Sans",sans-serif;line-height:1}
.site-logo .name-main{display:block;font-size:31px;letter-spacing:1px}
.site-logo .name-sub{display:block;font-size:16px;letter-spacing:2px;margin-top:2px}
.main-nav{position:absolute;top:35px;left:429px;display:flex;list-style:none}
.main-nav li{height:28px;line-height:28px;padding:0 10px;margin-right:12px;color:#fff;font-weight:700;font-size:11.5px;border-radius:4px;white-space:nowrap}
.main-nav li:last-child{margin-right:0}
.main-nav li.active{background:var(--nav-active)}
.hero{position:absolute;left:104px;top:100px;width:996px;height:340px;background:#fff;border-radius:10px 10px 0 0;overflow:hidden}
.hero-visual{position:absolute;left:8px;top:30px;width:662px;height:310px;background:linear-gradient(100deg,#e8ecef 0%,#5aa1c9 45%,#2a2a2e 85%)}
.partner{position:absolute;right:16px;top:24px;display:flex;align-items:center;gap:10px;color:var(--brand-red);font-size:26px}
.partner .sq{width:30px;height:30px;background:var(--brand-red)}
.hero-copy{position:absolute;left:694px;top:103px;width:287px}
.hero-copy h1{font-family:Arimo,Arial,sans-serif;font-weight:400;color:var(--brand-blue);font-size:21px;line-height:21px}
.hero-copy hr{border:0;border-top:1px dashed #aaa;margin:18px 0 11px}
.hero-copy p{font-size:12px;line-height:20px;text-align:justify}
.about{position:absolute;left:106px;top:466px;width:724px}
.about h2{color:var(--brand-blue);font-weight:400;font-size:20px;margin-bottom:9px}
.about p{font-size:11.5px;line-height:16px;text-align:justify;margin-bottom:17px}
.feature{position:absolute;top:667px;height:220px;padding:9px 10px}
.feature h3{font-size:20px;font-weight:700}
.feature.green{left:109px;width:340px;background:var(--green-box)}
.feature.green h3{color:var(--green-title)}
.feature.green p{margin-top:12px;font-size:11.5px;line-height:19px;text-align:justify;padding-right:5px}
.learn-more{position:absolute;left:195px;top:177px;width:130px;height:30px;background:#555;border-radius:5px;color:#fff;font-weight:700;font-size:12px;text-align:center;line-height:30px}
.feature.blue{left:480px;width:350px;background:var(--blue-box)}
.feature.blue h3{color:var(--blue-title)}
.feature.blue ul{list-style:none;margin-top:2px}
.feature.blue li{font-size:11.5px;line-height:24px;color:var(--blue-title);white-space:nowrap}
.feature.blue li b{color:var(--brand-red)}
.sidebar{position:absolute;left:860px;top:462px;width:238px;height:426px;border:1px solid #ddd;border-radius:6px;overflow:hidden}
.sidebar h4{background:#222;color:#fff;font-weight:400;font-size:20px;height:36px;line-height:36px;padding-left:12px}
.sidebar ul{list-style:none;padding:3px 10px 0 28px}
.sidebar li{position:relative;height:28px;line-height:28px;color:var(--link);border-bottom:1px solid #ddd;padding-left:4px}
.sidebar li::before{content:"";position:absolute;left:-16px;top:7px;width:13px;height:13px;border-radius:50%;border:1px solid #bbb;background:#f3f3f3}
.sidebar li::after{content:"";position:absolute;left:-11px;top:11px;border-left:4px solid #2a7bb0;border-top:3px solid transparent;border-bottom:3px solid transparent}
.site-footer{position:absolute;left:0;top:920px;width:1200px;height:81px;background:var(--footer)}
.footer-nav{position:absolute;left:118px;top:35px;display:flex;list-style:none;color:#fff;font-size:11px}
.footer-nav li{margin-right:25px;white-space:nowrap}
.copyright{position:absolute;right:116px;top:35px;color:var(--copyright);font-size:11px}
</style>
</head>
<body>
<div class="top-strip"></div>
<header class="masthead">
  <div class="site-logo"><span class="dot"></span><span class="name"><span class="name-main">QUILLPAGE</span><span class="name-sub">WORDS</span></span></div>
  <ul class="main-nav">
    <li>HOME</li><li class="active">ABOUT US</li><li>SERVICES</li><li>SAMPLES</li><li>PRICING</li><li>CLIENTS</li><li>CAREER</li><li>CONTACT US</li>
  </ul>
</header>
<section class="hero">
  <div class="hero-visual" role="img" aria-label="Word grid spelling quality, creativity, delivery, service, expertise, integrity and originality beside a smiling businessman holding a clipboard"></div>
  <div class="partner"><span class="sq"></span><span>Corvella</span></div>
  <div class="hero-copy">
    <h1>Donec at tortor eget quam ultrices sollicitudin.</h1>
    <hr>
    <p><b>Ut ullamcorper</b> adipiscing nisl id pretium. In est nisl, aliquam non molestie vitae, laoreet sit amet lectus. Donec quis neque eget arcu dapibus cursus ut a dolor. Duis facilisis sagittis metus, in ultrices lacus tincidunt malesuada. Vestibulum ante ipsum primis in faucibus.</p>
  </div>
</section>
<main>
  <section class="about">
    <h2>ABOUT US</h2>
    <p>Integer non ligula at metus dictum imperdiet vel id nulla. Phasellus urna tellus, sollicitudin quis tincidunt vel, iaculis varius velit. Vestibulum fringilla orci a felis rhoncus nec adipiscing ipsum vestibulum. Vestibulum tempus varius pellentesque. Cras placerat ante a turpis vestibulum sed aliquet felis tempus. Sed adipiscing convallis velit. Duis tempor dolor ac tellus dapibus id sodales libero auctor. Sed ornare elementum dolor quis convallis. Phasellus sed lorem odio, in vulputate nisi. Morbi at neque quis turpis pharetra adipiscing. Phasellus eu fermentum nunc.</p>
    <p>Morbi vulputate enim commodo nisl semper ultrices. Aliquam laoreet porta nisi id vulputate. Aliquam in semper metus. Integer mattis fringilla felis id sodales. Nulla posuere molestie odio eget malesuada. Quisque et enim elit, ac porta est. Integer ut pretium nibh. Fusce et sapien eu ipsum malesuada.</p>
  </section>
  <section class="feature green">
    <h3>Metus dictum imperdiet</h3>
    <p>Integer non ligula at metus dictum imperdiet vel id nulla. Phasellus urna tellus, sollicitudin quis tincidunt vel, iaculis varius velit. Vestibulum fringilla orci a felis rhoncus nec adipiscing ipsum vestibulum. Vestibulum tempus varius pellentesque. Cras placerat ante a turpis vestibulum sed aliquet felis tempus. Phasellus sed lorem odio, in vulputate nisi. Morbi at neque quis.</p>
    <div class="learn-more">LEARN MORE ››</div>
  </section>
  <section class="feature blue">
    <h3>Sed adipiscing convallis</h3>
    <ul>
      <li><b>››</b> Vivamus ut risus sem, vitae bibendum augue.</li>
      <li><b>››</b> Sed consectetur purus non magna imperdiet non pharetra</li>
      <li><b>››</b> Donec eget quam nunc, a adipiscing urna.</li>
      <li><b>››</b> Maecenas facilisis lorem ac massa tincidunt rutrum.</li>
      <li><b>››</b> Suspendisse posuere lectus eu nunc</li>
      <li><b>››</b> Nulla tempus ultricies ligula, mollis tempus nunc</li>
      <li><b>››</b>Proin et orci quis nisi placerat aliquam sed sed erat.</li>
    </ul>
  </section>
  <aside class="sidebar">
    <h4>Our Services</h4>
    <ul>
      <li>Lorem</li><li>Ut in erat</li><li>Sed egestas</li><li>Duis eget lectus</li><li>Quisque tempus</li><li>Phasellus</li><li>Suspendisse</li><li>Aliquam hendrerit</li><li>Fusce sagittis</li><li>Cras scelerisque</li><li>Morbi id risus</li><li>In ultrices</li><li>Fusce</li>
    </ul>
  </aside>
</main>
<footer class="site-footer">
  <ul class="footer-nav">
    <li>HOME</li><li>ABOUT US</li><li>SERVICES</li><li>SAMPLES</li><li>PRICING</li><li>CLIENTS</li><li>CAREER</li><li>CONTACT US</li>
  </ul>
  <div class="copyright">Copyright © 2011 Quillpagewords.com</div>
</footer>
</body>
</html>
```